Autism Support Coach needs Advertisement Design

I need an ad that fits in the feel of the "Save the Date" picture attached below. My business will be a sponsor and also advertising in the gala's magazine. I would like my original colors of orange and maroon red to be the standout colors. Phone number, website and Chatterfold should be somewhere at the bottom maybe. I am open to variations of background color in the oranges and maroon reds if you think it will look good. Dimensions should be: 4-1/2”h x 6” w
Thank you!!!

Target Market(s)

Autism Fundraising Gala with a Ruby theme

Industry/Entity Type

Advertising

Font styles to use
Script

Requirements
Must have
• The tag line should be:
• Autism Support Coaching
• Phone: 734-615-2089
• torvelancoaching.com
• Follow us on Chatterfold.com/Torvelancoachingautism

```html
<!DOCTYPE html>
<html lang="en">
<head>
<meta charset="utf-8">
<title>Torvelan Coaching Services – Ad</title>
<link rel="stylesheet" href="https://fonts.googleapis.com/css2?family=Great+Vibes&family=Open+Sans:wght@400;600;700;800&display=swap">
<style>
  :root {
    --maroon: #a3161b;
    --orange: #f26a21;
    --orange-light: #f7962d;
    --ink: #2f2f2f;
    --paper: #fbf8f3;
    --white: #ffffff;
    --skin: #c99275;
    --hair: #4a2a1c;
  }
  * { margin: 0; padding: 0; box-sizing: border-box; }
  html, body { width: 1200px; height: 900px; overflow: hidden; background: var(--paper); }
  .ad {
    position: relative; width: 1200px; height: 900px; overflow: hidden;
    background: radial-gradient(ellipse at 50% 35%, #ffffff 0%, var(--paper) 70%, #efe8dc 100%);
    font-family: "Open Sans", Arial, sans-serif; color: var(--ink);
  }
  .copy { position: absolute; left: 0; right: 0; top: 0; text-align: center; }
  .section-title { color: var(--maroon); font-weight: 800; font-size: 38px; letter-spacing: 0.5px; line-height: 1.2; }
  .feelings .section-title { margin-top: 26px; }
  .item { margin-top: 8px; }
  .item-title { color: var(--orange); font-weight: 700; font-size: 26px; line-height: 1.25; }
  .item-text { font-size: 25px; line-height: 1.3; }
  .hopes .item-title { font-size: 31px; }
  .hopes .item { margin-top: 12px; }
  .hopes-title { display: flex; align-items: center; justify-content: center; gap: 18px; margin-top: 24px; }
  .hopes-title .rule { width: 110px; height: 4px; background: var(--maroon); }
  .band { position: absolute; left: 0; top: 0; }
  .portrait {
    position: absolute; left: 1010px; top: 540px; width: 190px; height: 360px;
    background: radial-gradient(ellipse at 55% 40%, var(--skin) 0%, #a8705a 45%, var(--hair) 80%);
    border-top-left-radius: 110px 120px;
  }
  .brand-mark {
    position: absolute; left: 42px; top: 462px; width: 116px; height: 116px; border-radius: 50%;
    background: var(--orange); border: 6px solid var(--white);
  }
  .brand { position: absolute; left: 30px; top: 734px; }
  .brand-name { color: var(--white); font-weight: 700; font-size: 52px; line-height: 1; }
  .brand-sub { color: var(--white); font-weight: 700; font-size: 19px; letter-spacing: 3px; margin-top: 6px; }
  .tagline { font-family: "Great Vibes", cursive; color: var(--white); font-size: 36px; line-height: 1.1; margin-top: 4px; }
  .contact { position: absolute; left: 418px; top: 718px; color: var(--white); }
  .contact .phone, .contact .web { font-size: 32px; line-height: 1.38; }
  .contact .social { font-size: 19px; margin-top: 6px; }
</style>
</head>
<body>
<div class="ad">
  <svg class="band" width="1200" height="900" viewBox="0 0 1200 900" aria-hidden="true">
    <defs>
      <linearGradient id="bandFill" x1="0" y1="0" x2="1" y2="0">
        <stop offset="0" stop-color="#f58a24"/>
        <stop offset="1" stop-color="#f26a21"/>
      </linearGradient>
    </defs>
    <path d="M0 700 C300 670 700 710 1200 650 L1200 900 L0 900 Z" fill="var(--maroon)"/>
    <path d="M0 718 C320 690 700 728 1200 670 L1200 900 L0 900 Z" fill="url(#bandFill)"/>
  </svg>

  <div class="portrait" role="img" aria-label="Photo of the coach, smiling, shoulders up"></div>

  <div class="copy">
    <section class="feelings">
      <h2 class="section-title">ARE YOU FEELING:</h2>
      <div class="item">
        <p class="item-title">Overwhelmed?</p>
        <p class="item-text">Your child's behavior seems unmanageable and you don't know where to turn?</p>
      </div>
      <div class="item">
        <p class="item-title">Helpless?</p>
        <p class="item-text">When your child acts out and people disapprove or stare?</p>
      </div>
      <div class="item">
        <p class="item-title">Anxious?</p>
        <p class="item-text">You don't know what will happen to your child if something happens to you?</p>
      </div>
    </section>
    <section class="hopes">
      <div class="hopes-title">
        <span class="rule"></span>
        <h2 class="section-title">IMAGINE FEELING:</h2>
        <span class="rule"></span>
      </div>
      <div class="item">
        <p class="item-title">Confident and In Control</p>
        <p class="item-text">Calmly using new skills to handle any situation!</p>
      </div>
      <div class="item">
        <p class="item-title">Understood and Supported</p>
        <p class="item-text">By realizing that openness and frank discussion helps!</p>
      </div>
      <div class="item">
        <p class="item-title">Positive and Optimistic</p>
        <p class="item-text">Knowing the future is going to OK!</p>
      </div>
    </section>
  </div>

  <div class="brand-mark"></div>
  <div class="brand">
    <p class="brand-name">Torvelan</p>
    <p class="brand-sub">COACHING SERVICES</p>
    <p class="tagline">Autism Support Coaching</p>
  </div>

  <div class="contact">
    <p class="phone">734-615-2089</p>
    <p class="web">www.torvelancoaching.com</p>
    <p class="social">Follow us on Chatterfold.com/Torvelancoachingautism</p>
  </div>
</div>
</body>
</html>
```